Fitness Equipment & Service

I want to make the card eye catching and fun. We are called Corvane Motion Limited and we are based in Wales. We sell, install and service all types of fitness equipment from Skipping ropes, right through the Dumbbells, Kettle bells and Barbells through to state of the art Treadmills, Running Machines and Strength Equipment. We also design and install changing room furniture and lockers.

TYPOGRAPHY
We would like to use Futrura. Futura has an appearance of efficiency and forwardness. The typeface is derived
from simple geometric forms (near-perfect circles, triangles and squares) and is based on strokes of
near-even weight, which are low in contrast. This is most visible in the almost perfectly round stroke of
the o, which is nonetheless slightly ovoid.
The lowercase has tall ascenders, which rise above the cap line. The uppercase
characters present proportions similar to those of classical Roman capitals.

TYPOGRAPHIC CONSIDERATIONS
No Strike though
No Horizontal Scaling
No Drop Shadows
No Effects
Never use less than 120% Leading

OUR CORPORATE COLOURS
BRAND GUIDELINES
We were thinking that our primary colour palette consists of the Acid Green (Pantone 382) and Process Black.

We work closely with tolbrook Ltd and would like to include their name on the card somewhere. I have attached images of the other brands that we work with as an idea or the small icons I have included that illustrate what we do?. I have very kindly been given permission to use any of the images off the files that I have included below, so I hope these help. I will include these below. I would be open to suggestions if it made the card more striking Can you do it?
Updates

Hi All, Just wanted to add a few thoughts but you are the guys with the creative visions (thats why are here) We are based in Wales, UK and we would be open to lots of different ideas on a theme but must be eye catching, Bold and FUN. If you can or think that the Welsh or any dragon could be put in there then go for it (its not a must have) We have also added some ideas for colour but again its over to you!! GO FOR IT ! Thanks and look forward to your visions! Owen

Hi All, Just thought I would sen through the contact details that need to be on the card. (if you want to play around with icons instead of the wording twitter, Facebook, go for it): Corvane Motion Limited Owen Pritchard Managing Director Mob: +44 (0)7382 519 046 e-mail: sales@corvanemotion.co.uk Web: Corvanemotion.co.uk twitter: @motionPostbag Facebook: Corvane Motion Limited

Industry/Entity Type

Fitness

```html
<!DOCTYPE html>
<html lang="en">
<head>
<meta charset="utf-8">
<title>Corvane Motion Limited – Business Card</title>
<link rel="stylesheet" href="https://fonts.googleapis.com/css2?family=Jost:wght@400;500;600&display=swap">
<style>
  :root {
    --acid: #c4d600;
    --acid-ink: #8c9a00;
    --black: #111111;
    --black-soft: #1e1f1c;
    --charcoal: #2b2d27;
    --ink: #2f302c;
    --rule: #d3d6c4;
    --paper: #ffffff;
    --backdrop: #e6e4df;
  }
  * { margin: 0; padding: 0; box-sizing: border-box; }
  html, body {
    width: 1200px; height: 950px; overflow: hidden;
    background: var(--backdrop);
    font-family: "Jost", sans-serif;
  }
  .canvas { position: relative; width: 1200px; height: 950px; }

  .card {
    position: absolute; width: 640px; height: 366px;
    border-radius: 4px;
    box-shadow: 0 10px 28px rgba(0,0,0,.2);
    overflow: hidden;
  }

  /* Reverse side */
  .card--back {
    left: 460px; top: 110px;
    background:
      linear-gradient(90deg, transparent 0 76%, rgba(43,45,39,.6) 92%, var(--charcoal) 100%),
      radial-gradient(circle at 42% 48%, #2f3414 0%, var(--black-soft) 40%, var(--black) 100%);
  }
  .back-mark {
    position: absolute; left: 50%; top: 40%; transform: translate(-50%, -50%);
    display: flex; align-items: center; gap: 14px;
  }
  .back-mark__dot {
    width: 54px; height: 54px; border-radius: 50%; background: var(--acid);
  }
  .back-mark__name {
    color: #ffffff; font-weight: 500; font-size: 24px; line-height: 1.25; white-space: nowrap;
  }
  .back-web {
    position: absolute; left: 360px; top: 252px;
    display: flex; align-items: center; gap: 8px;
    color: var(--acid); font-size: 15px; line-height: 1.3; letter-spacing: .04em;
  }
  .back-web::after {
    content: ""; width: 40px; height: 1px; background: var(--acid);
  }
  .back-partner {
    position: absolute; left: 360px; top: 280px;
    color: rgba(255,255,255,.75); font-size: 13px; line-height: 1.3; letter-spacing: .04em;
  }

  /* Front side */
  .card--front {
    left: 120px; top: 420px;
    background: var(--paper);
  }
  .brand {
    position: absolute; left: 36px; top: 34px;
    display: flex; align-items: center; gap: 14px;
  }
  .brand__dot { width: 70px; height: 70px; border-radius: 50%; background: var(--acid); }
  .brand__name {
    color: var(--black); font-weight: 600; font-size: 20px; line-height: 1.25; width: 150px;
  }
  .divider {
    position: absolute; left: 30px; right: 30px; top: 176px;
    height: 1px; background: var(--rule);
  }
  .contacts {
    position: absolute; left: 34px; top: 192px; list-style: none;
    color: var(--ink); font-size: 16px; line-height: 1.35;
  }
  .contacts li { display: flex; align-items: center; gap: 9px; }
  .contacts svg { width: 14px; height: 14px; fill: var(--black); flex: none; }

  .person {
    position: absolute; right: 34px; top: 226px; text-align: right;
    border-bottom: 1px solid var(--rule); padding-bottom: 6px; width: 220px;
  }
  .person__name { color: var(--black); font-weight: 600; font-size: 22px; line-height: 1.2; }
  .person__role { color: var(--acid-ink); font-size: 17px; line-height: 1.25; }
  .social {
    position: absolute; right: 34px; top: 298px; display: flex; gap: 6px;
  }
  .social span { width: 14px; height: 14px; border-radius: 2px; background: var(--black); }
  .address {
    position: absolute; right: 34px; top: 318px; text-align: right;
    color: var(--ink); font-size: 15px; line-height: 1.3; font-style: normal;
  }
  .accent-bar {
    position: absolute; right: 0; top: 226px; width: 8px; height: 48px; background: var(--acid);
  }
</style>
</head>
<body>
<main class="canvas">

  <section class="card card--back" aria-label="Card reverse">
    <div class="back-mark">
      <span class="back-mark__dot"></span>
      <span class="back-mark__name">Corvane Motion Limited</span>
    </div>
    <p class="back-web">Corvanemotion.co.uk</p>
    <p class="back-partner">In partnership with tolbrook Ltd</p>
  </section>

  <section class="card card--front" aria-label="Card front">
    <div class="brand">
      <span class="brand__dot"></span>
      <span class="brand__name">Corvane Motion Limited</span>
    </div>

    <div class="divider"></div>

    <ul class="contacts">
      <li>
        <svg viewBox="0 0 14 14" aria-hidden="true"><path d="M4 0h6a1 1 0 0 1 1 1v12a1 1 0 0 1-1 1H4a1 1 0 0 1-1-1V1a1 1 0 0 1 1-1zm0 2v9h6V2z"/></svg>
        +44 (0)7382 519 046
      </li>
      <li>
        <svg viewBox="0 0 14 14" aria-hidden="true"><path d="M0 3h14v8H0zm1 1v.3l6 3.6 6-3.6V4zm0 1.5V10h12V5.5L7 9z"/></svg>
        sales@corvanemotion.co.uk
      </li>
      <li>
        <svg viewBox="0 0 14 14" aria-hidden="true"><circle cx="7" cy="7" r="6.5"/></svg>
        Corvanemotion.co.uk
      </li>
    </ul>

    <div class="person">
      <p class="person__name">Owen Pritchard</p>
      <p class="person__role">Managing Director</p>
    </div>
    <div class="accent-bar"></div>

    <div class="social" aria-hidden="true"><span></span><span></span></div>

    <address class="address">
      27 Harbour Row<br>Penarth, CF64 3AB
    </address>
  </section>

</main>
</body>
</html>
```